Surveillance Sign

Design sign and stickers with a line drawing of the camera.

Industry/Entity Type

Camera

Requirements
• I like this design: http://www.brevondo.com/cctv-camera-warning-signs-decals/camera-surveillance-sign

```html
<!DOCTYPE html>
<html lang="en">
<head>
<meta charset="UTF-8">
<title>Surveillance Sign</title>
<link href="https://fonts.googleapis.com/css2?family=Alfa+Slab+One&family=Rubik:wght@900&family=Mulish:wght@800;900&display=swap" rel="stylesheet">
<style>
  :root {
    --sign-red: #be1e24;
    --sign-yellow: #fff000;
    --alert-red: #ec1c24;
    --ink: #0d0d0d;
    --white: #ffffff;
    --camera-grey: #9a9a9c;
  }
  html, body {
    margin: 0;
    padding: 0;
    width: 1161px;
    height: 1200px;
    overflow: hidden;
    background: var(--white);
  }
  .sign {
    position: absolute;
    left: 211px;
    top: 130px;
    width: 740px;
    height: 941px;
    background: var(--sign-yellow);
    overflow: hidden;
  }
  .sign__backdrop {
    position: absolute;
    inset: 0;
  }
  .sign__header {
    position: absolute;
    left: 0;
    top: 0;
    width: 100%;
    height: 100px;
    background: var(--sign-red);
    display: flex;
    align-items: center;
    justify-content: center;
  }
  .sign__title {
    margin: 0;
    font-family: "Alfa Slab One", serif;
    font-size: 58px;
    letter-spacing: 2px;
    color: var(--sign-yellow);
    line-height: 1;
  }
  .sign__headline {
    position: absolute;
    left: 0;
    top: 128px;
    width: 100%;
    margin: 0;
    text-align: center;
    font-family: "Rubik", sans-serif;
    font-weight: 900;
    font-size: 80px;
    line-height: 74px;
    letter-spacing: -2px;
    text-transform: uppercase;
  }
  .sign__headline-line { display: block; }
  .sign__headline-line--dark { color: var(--ink); }
  .sign__headline-line--alert { color: var(--alert-red); }
  .sign__camera {
    position: absolute;
    left: 93px;
    top: 450px;
    width: 569px;
    height: 316px;
    border-radius: 40px 120px 160px 40px;
    background: linear-gradient(160deg, #d8d8da 0%, var(--camera-grey) 45%, #2a2a2a 100%);
  }
  .sign__notice {
    position: absolute;
    left: 0;
    top: 797px;
    width: 100%;
    margin: 0;
    text-align: center;
    font-family: "Mulish", sans-serif;
    font-weight: 900;
    font-size: 21px;
    line-height: 26px;
    color: var(--white);
    text-transform: uppercase;
  }
  .sign__footer {
    position: absolute;
    left: 0;
    top: 882px;
    width: 100%;
    height: 59px;
    background: var(--ink);
    display: flex;
    align-items: center;
    justify-content: center;
  }
  .sign__url {
    font-family: "Mulish", sans-serif;
    font-weight: 900;
    font-size: 25px;
    letter-spacing: 3.5px;
    color: var(--sign-yellow);
  }
</style>
</head>
<body>
  <div class="sign">
    <svg class="sign__backdrop" width="740" height="941" viewBox="0 0 740 941" aria-hidden="true">
      <polygon points="0,566 740,790 740,941 0,941" fill="var(--sign-red)"/>
    </svg>

    <header class="sign__header">
      <h1 class="sign__title">SURVEILLANCE</h1>
    </header>

    <h2 class="sign__headline">
      <span class="sign__headline-line sign__headline-line--dark">This property</span>
      <span class="sign__headline-line sign__headline-line--dark">protected by</span>
      <span class="sign__headline-line sign__headline-line--alert">CCTV security</span>
      <span class="sign__headline-line sign__headline-line--alert">cameras</span>
    </h2>

    <div class="sign__camera" role="img" aria-label="Illustration of a wall-mounted CCTV bullet camera with infrared LED ring"></div>

    <p class="sign__notice">
      For your personal protection all activities are<br>
      recorded on digitalmedia to aid in the prosecution<br>
      of any crime committed on this property.
    </p>

    <footer class="sign__footer">
      <span class="sign__url">www.brevondo.com</span>
    </footer>
  </div>
</body>
</html>
```